B2B Energy Broker Website

Our current website looks amateur, we need something far more professional looking and advanced. Current website is www.kelmora-utilitylink.com

```html
<!DOCTYPE html>
<html lang="en">
<head>
<meta charset="utf-8">
<title>Kelmora Utility Link – B2B Energy Broker</title>
<link href="https://fonts.googleapis.com/css2?family=Lato:wght@300;400;700;900&display=swap" rel="stylesheet">
<style>
:root{
  --navy:#1d1f47;
  --navy-deep:#15173a;
  --ink:#2b2b2b;
  --text:#555a60;
  --muted:#8a8f96;
  --line:#d6d8dc;
  --grey-bg:#e7e8ea;
  --light-bg:#f3f4f5;
  --white:#ffffff;
  --accent:#2f6fd6;
  --btn:#2b2d31;
}
*{box-sizing:border-box;margin:0;padding:0}
html,body{width:1200px;height:3448px;overflow:hidden}
body{font-family:"Lato",Arial,sans-serif;color:var(--text);background:var(--white);position:relative}
section,header,footer{position:absolute;left:0;width:1200px}
.btn{display:inline-block;background:var(--btn);color:var(--white);font-size:14px;font-weight:700;padding:11px 24px;border-radius:20px;letter-spacing:.3px}

/* Header */
.site-header{top:0;height:72px;background:var(--white);border-bottom:1px solid var(--line)}
.brand{position:absolute;left:120px;top:16px;display:flex;align-items:center;gap:10px}
.brand-dot{width:38px;height:38px;border-radius:50%;background:var(--navy)}
.brand-name{font-size:20px;font-weight:700;color:var(--navy);letter-spacing:3px;line-height:1}
.brand-name small{display:block;font-size:11px;letter-spacing:.5px;font-weight:700;margin-top:3px}
.nav{position:absolute;left:336px;top:0;display:flex;height:72px;align-items:center;gap:34px;font-size:14px;color:var(--ink)}
.nav .active{font-weight:700;border-bottom:3px solid var(--navy);padding:25px 0 23px}
.head-right{position:absolute;right:120px;top:0;height:72px;display:flex;align-items:center;gap:22px}
.head-phone{font-size:14px;color:var(--ink);display:flex;align-items:center;gap:6px;white-space:nowrap}
.head-social{display:flex;gap:8px}
.head-social span{width:20px;height:20px;background:var(--navy);border-radius:3px}

/* Hero */
.hero{top:72px;height:528px;overflow:hidden}
.hero-photo{position:absolute;inset:0;background:linear-gradient(180deg,#6d7d97 0%,#8d9ab0 30%,#6a7386 55%,#3a3c4c 80%,#2a2b38 100%)}
.hero-text{position:absolute;left:120px;top:132px;color:var(--white);width:440px}
.hero-text h1{font-size:40px;font-weight:900;line-height:1.08;letter-spacing:.5px}
.hero-text h2{font-size:15px;font-weight:700;letter-spacing:1.5px;margin-top:12px}
.hero-text p{font-size:13px;line-height:1.55;margin-top:14px;opacity:.9;width:300px}
.hero-text .btn{margin-top:76px}
.hero-arrow{position:absolute;top:290px}

/* Welcome */
.welcome{top:600px;height:520px;background:var(--white)}
.welcome-photo{position:absolute;left:120px;top:110px;width:440px;height:340px;border-radius:60px 0 60px 0;background:linear-gradient(160deg,#7fb3e3 0%,#b5d2ec 45%,#5b6b84 75%,#3a4256 100%)}
.welcome-text{position:absolute;left:610px;top:150px;width:470px}
.eyebrow{font-size:22px;color:var(--ink)}
.welcome-text h2{font-size:34px;font-weight:900;color:var(--ink);margin-top:8px;letter-spacing:.3px}
.welcome-text p{font-size:13px;line-height:1.6;margin-top:14px;text-align:justify}
.welcome-text .btn{margin-top:22px}

/* Section title */
.section-title{display:flex;align-items:center;justify-content:center;gap:16px;font-size:28px;font-weight:700;color:var(--ink)}
.section-title::before,.section-title::after{content:"";width:60px;height:2px;background:var(--ink)}

/* Services */
.services{top:1120px;height:600px;background:linear-gradient(180deg,#eceef0 0%,#dfe2e6 55%,#eef0f2 100%)}
.services .section-title{position:absolute;top:60px;width:100%}
.service{position:absolute;width:300px}
.service h3{font-size:16px;font-weight:900;color:var(--ink);letter-spacing:.3px}
.service p{font-size:12.5px;line-height:1.55;margin-top:6px}
.service.left{text-align:right;left:110px}
.service.right{left:790px}
.hub{position:absolute;left:0;top:0}

/* How it works */
.how{top:1720px;height:560px;background:linear-gradient(180deg,#fbfbfc 0%,#eef0f2 100%)}
.how .section-title{position:absolute;top:56px;width:100%}
.how-card{position:absolute;top:140px;width:300px;height:380px;background:var(--white);border:2px solid var(--ink);border-radius:18px;text-align:center;padding:46px 28px 0}
.how-card.featured{border-color:var(--accent)}
.how-icon{width:92px;height:92px;border-radius:50%;background:var(--btn);margin:0 auto;display:flex;align-items:center;justify-content:center}
.how-card h3{font-size:19px;font-weight:700;color:var(--ink);margin-top:28px}
.how-card p{font-size:13px;line-height:1.6;margin-top:18px}

/* FAQ */
.faq{top:2280px;height:720px;background:var(--grey-bg)}
.faq .section-title{position:absolute;top:72px;width:100%}
.faq-item{position:absolute;left:120px;width:960px;background:var(--white);border:1px solid var(--line);border-radius:4px}
.faq-q{display:flex;justify-content:space-between;align-items:center;height:62px;padding:0 26px;font-size:16px;color:var(--ink)}
.faq-q b{font-size:22px;font-weight:400}
.faq-a{border-top:1px solid var(--line);margin:0 26px;padding:20px 0 24px;font-size:13px;line-height:1.65}

/* Footer */
.site-footer{top:3000px;height:448px;background:var(--navy);color:#c9cbe0}
.foot-col{position:absolute;top:60px}
.foot-brand .brand-name{color:var(--white)}
.foot-brand .brand-dot{background:var(--white)}
.foot-brand p{font-size:12.5px;line-height:1.6;margin-top:18px;width:220px}
.foot-col h4{font-size:16px;font-weight:700;color:var(--white);margin-bottom:16px}
.foot-col ul{list-style:none;font-size:13px;line-height:2.1}
.contact-row{display:flex;gap:12px;font-size:13px;line-height:1.55;margin-bottom:14px}
.contact-row svg{flex:none;margin-top:2px}
.foot-social{display:flex;gap:18px}
.foot-social span{width:18px;height:18px;background:#c9cbe0;border-radius:50%}
.copyright{position:absolute;left:0;bottom:0;width:100%;height:58px;background:var(--navy-deep);text-align:center;line-height:58px;font-size:13px;color:var(--white);border-top:1px solid #2e3160}
</style>
</head>
<body>

<header class="site-header">
  <div class="brand"><span class="brand-dot"></span><span class="brand-name">KELMORA<small>utility link</small></span></div>
  <nav class="nav"><span class="active">Home</span><span>About Us</span><span>Services</span><span>FAQs</span><span>Contact Us</span></nav>
  <div class="head-right">
    <div class="head-phone">
      <svg width="14" height="14" viewBox="0 0 24 24"><path d="M6.6 10.8a15 15 0 0 0 6.6 6.6l2.2-2.2a1 1 0 0 1 1-.25 11.4 11.4 0 0 0 3.6.6 1 1 0 0 1 1 1V20a1 1 0 0 1-1 1A17 17 0 0 1 3 4a1 1 0 0 1 1-1h3.5a1 1 0 0 1 1 1c0 1.25.2 2.45.6 3.6a1 1 0 0 1-.25 1z" fill="#2b2b2b"/></svg>
      +1 (555) 014 2297
    </div>
    <div class="head-social"><span></span><span></span><span></span></div>
  </div>
</header>

<section class="hero">
  <div class="hero-photo" role="img" aria-label="Snow-capped mountain peak under a blue-grey sky"></div>
  <svg class="hero-arrow" style="left:60px" width="24" height="40" viewBox="0 0 24 40"><path d="M18 6 6 20l12 14" stroke="#fff" stroke-width="3" fill="none"/></svg>
  <svg class="hero-arrow" style="left:1116px" width="24" height="40" viewBox="0 0 24 40"><path d="M6 6l12 14L6 34" stroke="#fff" stroke-width="3" fill="none"/></svg>
  <div class="hero-text">
    <h1>TRANSPARENT<br>ENERGY SAVINGS</h1>
    <h2>UNBIASED FOR YOUR BUSINESS</h2>
    <p>Clear advice on gas and electricity contracts, with honest pricing and support that puts your business first every time.</p>
    <span class="btn">Get Started</span>
  </div>
</section>

<section class="welcome">
  <div class="welcome-photo" role="img" aria-label="Two engineers installing solar panels on a roof"></div>
  <div class="welcome-text">
    <div class="eyebrow">Welcome To —</div>
    <h2>KELMORA UTILITY LINK</h2>
    <p>Along with providing competitive business energy procurement, we run a complete service solution for your ongoing energy requirements. We can take total management of your bills, supplier relationship, renewals and more. If you are concerned about a more complex arrangement for your energy supply then we will endeavour to take over the time spent on it and allow you as much or as little involvement as you desire.</p>
    <span class="btn">Learn More</span>
  </div>
</section>

<section class="services">
  <div class="section-title">Our Services</div>
  <svg class="hub" width="1200" height="600" viewBox="0 0 1200 600">
    <circle cx="600" cy="300" r="112" fill="none" stroke="#2b2d31" stroke-width="2" stroke-dasharray="6 6"/>
    <circle cx="600" cy="300" r="66" fill="#2b2d31"/>
    <circle cx="600" cy="300" r="52" fill="none" stroke="#4a4d54" stroke-width="2"/>
    <g fill="#fff" stroke="#2b2d31" stroke-width="2">
      <circle cx="486" cy="198" r="22"/><circle cx="714" cy="198" r="22"/>
      <circle cx="486" cy="402" r="22"/><circle cx="714" cy="402" r="22"/>
    </g>
    <g stroke="#2b2d31" stroke-width="2" fill="none">
      <path d="M486 188c-6 8-7 13 0 20 7-7 6-12 0-20z"/>
      <path d="M714 187c-6 7-8 12-4 18 4 4 8 4 10 0 2-5 0-10-6-18z"/>
      <path d="M478 398h16M478 404h16M482 394v14M490 394v14"/>
      <path d="M716 390l-8 13h7l-3 11 9-14h-7z"/>
    </g>
  </svg>
  <div class="service left" style="top:160px"><h3>COMMERCIAL WATER</h3><p>The commercial water market has now been de-regulated. Speak to our team to find out how we can save you money on your water and waste bills.</p></div>
  <div class="service right" style="top:160px"><h3>COMMERCIAL GAS</h3><p>We offer an impartial review of your business gas requirements to ensure you are getting the best prices, service and management as a total package.</p></div>
  <div class="service left" style="top:360px"><h3>UTILITY SERVICES</h3><p>We can provide a wide range of business utility management services to save your time and money in a better spent.</p></div>
  <div class="service right" style="top:360px"><h3>COMMERCIAL ELECTRICITY</h3><p>We offer an impartial review of your business electricity requirements to ensure you are getting the best prices, service and management as a total.</p></div>
</section>

<section class="how">
  <div class="section-title">How its Work</div>
  <div class="how-card" style="left:112px">
    <div class="how-icon"><svg width="44" height="44" viewBox="0 0 44 44" fill="none" stroke="#fff" stroke-width="2.5"><path d="M6 38h32"/><path d="M10 34V24M18 34V18M26 34V22M34 34V12"/><path d="M8 20l10-8 8 6 10-10"/></svg></div>
    <h3>Market Trend Analysis</h3>
    <p>Our energy analysts monitor a live energy market curve to ensure you buy at the right time and save as much as possible.</p>
  </div>
  <div class="how-card featured" style="left:450px">
    <div class="how-icon"><svg width="46" height="40" viewBox="0 0 46 40" fill="none" stroke="#fff" stroke-width="2.5"><path d="M4 14l8-6 8 4 6-4 8 4 8-4"/><path d="M12 24l6 6 4-2 4 4 8-6-10-10-6 4"/><path d="M4 14l6 14M42 12l-6 16"/></svg></div>
    <h3>Direct Relationships</h3>
    <p>We hold direct relationships with over 30 major suppliers, so we use these relationships to ensure you get the most from your supplier.</p>
  </div>
  <div class="how-card" style="left:788px">
    <div class="how-icon"><svg width="44" height="44" viewBox="0 0 44 44" fill="none" stroke="#fff" stroke-width="2.5"><circle cx="22" cy="16" r="9"/><path d="M16 24l-4 14 10-4 10 4-4-14"/></svg></div>
    <h3>Industry Experience</h3>
    <p>Our two founders hold over 30 years industry experience between them and our staff are what we believe to be the best in the industry.</p>
  </div>
</section>

<section class="faq">
  <div class="section-title">Frequently asked questions</div>
  <div class="faq-item" style="top:140px">
    <div class="faq-q">why should my business use kelmora utility link? <b>⌃</b></div>
    <div class="faq-a">We provide an unbiased &amp; transparent cost effective solution to all your business energy needs. In essence, with over 3 decades experience in the UK energy industry. We have both the expertise &amp; know how to manage your business energy requirements. Our philosophy is simple solutions with transparency.</div>
  </div>
  <div class="faq-item" style="top:330px"><div class="faq-q">Who should consider using Kelmora Utility Link? <b>+</b></div></div>
  <div class="faq-item" style="top:410px"><div class="faq-q">Is Kelmora Utility Link independent? <b>+</b></div></div>
  <div class="faq-item" style="top:490px"><div class="faq-q">Will there be a charge for gaining quotations? <b>+</b></div></div>
</section>

<footer class="site-footer">
  <div class="foot-col foot-brand" style="left:120px">
    <div class="brand" style="position:static"><span class="brand-dot"></span><span class="brand-name">KELMORA<small>utility link</small></span></div>
    <p>Kelmora Utility Link was founded on a wealth of 30 years of commercial energy expertise with a mission to provide customers with a fresh approach to business utility services.</p>
  </div>
  <div class="foot-col" style="left:430px">
    <h4>Quick link</h4>
    <ul><li>Home</li><li>About Us</li><li>Services</li><li>FAQs</li><li>Contact Us</li></ul>
  </div>
  <div class="foot-col" style="left:620px;width:220px">
    <h4>Contact Us</h4>
    <div class="contact-row"><svg width="14" height="16" viewBox="0 0 14 16"><path d="M7 0a6 6 0 0 0-6 6c0 4.5 6 10 6 10s6-5.5 6-10a6 6 0 0 0-6-6zm0 8.5A2.5 2.5 0 1 1 7 3.5a2.5 2.5 0 0 1 0 5z" fill="#c9cbe0"/></svg><span>Unit 4<br>12 Harrow Lane<br>Brackford BK2 7QT</span></div>
    <div class="contact-row"><svg width="14" height="14" viewBox="0 0 24 24"><path d="M6.6 10.8a15 15 0 0 0 6.6 6.6l2.2-2.2a1 1 0 0 1 1-.25 11.4 11.4 0 0 0 3.6.6 1 1 0 0 1 1 1V20a1 1 0 0 1-1 1A17 17 0 0 1 3 4a1 1 0 0 1 1-1h3.5a1 1 0 0 1 1 1c0 1.25.2 2.45.6 3.6a1 1 0 0 1-.25 1z" fill="#c9cbe0"/></svg><span>+1 (555) 014 2297</span></div>
    <div class="contact-row"><svg width="14" height="12" viewBox="0 0 14 12"><rect x=".5" y=".5" width="13" height="11" rx="1" fill="none" stroke="#c9cbe0"/><path d="M1 1l6 5 6-5" fill="none" stroke="#c9cbe0"/></svg><span>info@kelmora-utilitylink.com</span></div>
  </div>
  <div class="foot-col" style="left:860px">
    <h4>Social Media</h4>
    <div class="foot-social"><span></span><span></span><span></span><span></span><span></span></div>
  </div>
  <div class="copyright">Copyright © 2022 Kelmora Utility Link - All Rights Reserved.</div>
</footer>

</body>
</html>
```